A WEBSITE FOR A JEWELLERY RETAIL STORE WITH A SHOPPING CART, AND ABILITY TO ORDER ONLINE.

I require a website with a shopping cart.

We sell MAINLY diamond jewellery (such as rings etc). I need it to be simple to change prices with only a few buttons, as the price fluctuates due to the US Dollar.

We are a diamond wholesaler, selling directly to the public, so we guarantee the lowest prices in Australia.

There is also a link to current inventory that will need to be uploaded to the site.

This could be an ongoing job, where you will be paid weekly to maintain and update the website if you wish.

Target Market(s)

People getting engaged, and wanting to buy a diamond ring.

Number of Pages Required

5+ page

Colors

Designer to choose colors to be used in the design.

Requirements
Must have
• elegant.
• modern.
• professional.
• SHOPPING CART.
• ABILITY TO SEARCH FOR LOOSE DIAMONDS (LINK THAT NEEDS TO BE EMBEDDED WILL BE SENT WHICH SHOWS CURRENT STOCK).
• ENGAGEMENT RINGS
• WEDDING RINGS
• DIAMOND EARRINGS
• DIAMOND PENDANTS
• LOOSE DIAMONDS.
• SALE ITEMS.
• OTHER JEWELLERY.
• EDUCATION
• WISH LIST
• CART.
Nice to have
• a good place to look for inspiration on pages is https://www.velmarigems.example.
• YOU MAY VISIT OUR FACEBOOK PAGE AT.
• HTTP://WWW.SOCIALPAGE.EXAMPLE/QUINTORAJEWELLERS
Should not have
• We don't want it too busy.

```html
<!DOCTYPE html>
<html lang="en">
<head>
<meta charset="utf-8">
<title>Education – Quintora Jewellers Australia</title>
<link rel="stylesheet" href="https://fonts.googleapis.com/css2?family=Jost:wght@300;400;500&family=Marcellus&display=swap">
<style>
:root{
  --ink:#1a1a1a;
  --black:#000;
  --white:#fff;
  --rule:#bdbdbd;
  --accent:#8a2a20;
  --band:#8b7866;
  --muted:#555;
}
*{box-sizing:border-box;margin:0;padding:0}
html,body{width:1200px;height:2811px;overflow:hidden;background:var(--white)}
body{position:relative;font-family:"Jost",sans-serif;color:var(--ink)}
.abs{position:absolute}

.promo-bar{left:0;top:0;width:1200px;height:61px;background:var(--black);color:var(--white);
  display:flex;align-items:center;justify-content:center;font-family:"Marcellus",serif;font-size:14px;letter-spacing:1.3px}

.country{left:34px;top:110px;font-size:15px;letter-spacing:1.4px;display:flex;align-items:center;gap:4px}
.country .select{border:1px solid #888;border-radius:6px;padding:1px 12px;font-size:14px}
.brand{left:452px;top:92px;width:281px;text-align:center}
.brand .name{display:flex;align-items:center;justify-content:center;gap:8px;font-size:21px;letter-spacing:.8px;font-weight:400;white-space:nowrap;line-height:30px}
.brand .name i{display:inline-block;width:20px;height:20px;background:var(--ink);flex:none}
.brand .rule{height:3px;background:#2a1414;margin-top:13px}
.brand .region{font-family:"Marcellus",serif;font-size:13px;letter-spacing:9px;margin-top:7px}
.account-links{right:40px;top:113px;display:flex;gap:26px;font-size:14px;letter-spacing:1.3px}

.hr{height:1px;background:var(--rule)}
.main-nav{left:43px;top:233px;display:flex;font-size:14px;letter-spacing:2px;white-space:nowrap}
.main-nav span{margin-right:36px}
.search{left:894px;top:234px;width:253px;border-bottom:1px solid #888;font-size:11px;letter-spacing:1.5px;padding-bottom:3px;color:#444}
.search svg{position:absolute;right:12px;top:-2px}

.crumb{left:58px;top:337px;font-size:14px;letter-spacing:1px}
.crumb b{font-weight:400;color:var(--accent)}

.photo{display:block}
.hero{left:33px;top:376px;width:1127px;height:423px;
  background:radial-gradient(ellipse at 30% 60%,#d8d8d8 0%,#8a8a8a 25%,#2a2a2a 55%,#050505 80%)}
.hero-panel{left:526px;top:491px;width:619px;height:194px;background:rgba(40,40,40,.78);color:var(--white);padding:0 27px}
.hero-panel h1{font-family:"Marcellus",serif;font-weight:400;font-size:28px;letter-spacing:1.5px;text-align:center;padding:17px 0 7px;border-bottom:1px solid #ccc}
.hero-panel p{font-size:20px;line-height:22.5px;letter-spacing:1px;text-align:justify;margin-top:13px;font-weight:300}

.section-title{font-family:"Marcellus",serif;font-size:25px;letter-spacing:2px;font-weight:400;text-align:center;width:1200px;left:0}
.feature-text{width:456px;font-size:13px;line-height:14.8px;letter-spacing:1px;text-align:justify;color:#333}
.btn{border:2px solid #222;display:flex;align-items:center;justify-content:center;font-size:12.5px;letter-spacing:1.5px;background:var(--white)}

.guide{width:300px;text-align:center}
.guide h3{font-family:"Marcellus",serif;font-weight:400;font-size:13px;letter-spacing:1px}
.guide-text{width:267px;font-size:6.6px;line-height:8.2px;letter-spacing:.5px;text-align:justify;color:#444}
.btn-small{width:124px;height:23px;border:2px solid #222;font-size:6.5px;letter-spacing:1px;display:flex;align-items:center;justify-content:center}

.newsletter{left:0;top:2438px;width:1200px;height:80px;background:var(--band);color:var(--white)}
.newsletter .label{font-family:"Marcellus",serif;font-size:19px;letter-spacing:2px;top:28px}
.newsletter .field{left:229px;top:21px;width:265px;height:36px;background:var(--white);color:#777;font-size:13.5px;letter-spacing:1px;padding:8px 7px;white-space:nowrap;overflow:hidden}
.newsletter .signup{left:494px;top:21px;width:131px;height:36px;background:var(--black);font-size:13.5px;letter-spacing:1px;display:flex;align-items:center;justify-content:center}
.social{top:25px;display:flex;gap:34px}
.social span{width:26px;height:26px;border-radius:50%;border:2px solid var(--black)}

.footer{left:0;top:2518px;width:1200px;height:293px;background:var(--black);color:var(--white)}
.footer .about{left:41px;top:35px;width:299px;font-size:14.5px;line-height:16.3px;letter-spacing:.9px;text-align:justify;color:var(--white)}
.footer .help{left:41px;top:202px;font-size:10px;letter-spacing:.8px;line-height:17px;color:var(--white)}
.footer .col{top:38px;font-size:13.5px;letter-spacing:1.2px;line-height:26px;color:var(--white)}
.footer .col h4{font-weight:400;font-size:15px;text-decoration:underline;margin-bottom:2px}
.footer .copy{left:0;width:1200px;top:243px;text-align:center;font-size:12.5px;letter-spacing:1.2px;color:var(--white)}
</style>
</head>
<body>

<header>
  <div class="abs promo-bar">ORDER NOW AND ENJOY FREE SWIFTPOST OVERNIGHT SHIPPING AND 30-DAY RETURNS</div>
  <div class="abs country">Select your country: <span class="select">$AUD ▾</span></div>
  <div class="abs brand">
    <div class="name"><i></i>QUINTORA JEWELLERS</div>
    <div class="rule"></div>
    <div class="region">AUSTRALIA</div>
  </div>
  <div class="abs account-links"><span>Register | Sign In</span><span>Wishlist ♥</span><span>Cart (0)</span></div>
  <div class="abs hr" style="left:0;top:208px;width:1200px"></div>
  <nav class="abs main-nav">
    <span>DIAMONDS</span><span>ENGAGEMENT RINGS</span><span>WEDDING</span><span>JEWELRY</span><span style="margin-left:12px">EDUCATION</span><span>ON SALE</span>
  </nav>
  <div class="abs search">Search
    <svg width="18" height="14" viewBox="0 0 18 14"><circle cx="6" cy="6" r="4.5" fill="none" stroke="#555" stroke-width="1.4"/><line x1="9.5" y1="9" x2="16" y2="13" stroke="#555" stroke-width="1.6"/></svg>
  </div>
  <div class="abs hr" style="left:0;top:298px;width:1200px"></div>
</header>

<main>
  <div class="abs crumb">Home &gt;&gt; <b>Education</b></div>

  <div class="abs photo hero" role="img" aria-label="Loose brilliant-cut diamonds scattered on a dark reflective surface"></div>
  <div class="abs hero-panel">
    <h1>EDUCATION</h1>
    <p>Lorem ipsum dolor sit amet, consectetur adipisicing elit, sed do eiusmod tempor incididunt ut labore et dolore magna aliqua. Ut enim ad minim veniam, quis nostrud exercitation ullamco laboris nisi ut aliquip ex</p>
  </div>

  <div class="abs hr" style="left:265px;top:850px;width:687px;background:#666"></div>
  <h2 class="abs section-title" style="top:874px;padding-left:10px">DIAMOND EDUCATION</h2>
  <div class="abs photo" style="left:177px;top:943px;width:416px;height:415px;background:linear-gradient(135deg,#f2f3f5,#c9ccd1 55%,#e6e7ea)" role="img" aria-label="Diamond gauge tool with loose diamonds and tweezers on brushed metal"></div>
  <p class="abs feature-text" style="left:649px;top:1041px">Lorem ipsum dolor sit amet, consectetur adipisicing elit, sed do eiusmod tempor incididunt ut labore et dolore magna aliqua. Ut enim ad minim veniam, quis nostrud exercitation ullamco laboris nisi ut aliquip ex ea commodo consequat. Duis aute irure dolor in reprehenderit in voluptate velit esse cillum dolore eu fugiat nulla pariatur. Excepteur sint occaecat cupidatat non proident, sunt in culpa qui officia deserunt mollit anim id est laborum. Sed ut perspiciatis unde omnis iste natus error sit voluptatem accusantium doloremque laudantium, totam rem aperiam, eaque ipsa quae ab</p>
  <div class="abs btn" style="left:772px;top:1205px;width:214px;height:42px">LEARN MORE</div>

  <div class="abs hr" style="left:265px;top:1415px;width:687px;background:#666"></div>
  <h2 class="abs section-title" style="top:1447px;padding-left:58px">ENGAGEMENT RING GUIDE</h2>
  <div class="abs photo" style="left:224px;top:1533px;width:321px;height:392px;background:radial-gradient(ellipse at 50% 50%,#b8b8bc,#e4e4e6 60%,#fafafa)" role="img" aria-label="Stack of diamond halo engagement rings and pavé bands"></div>
  <p class="abs feature-text" style="left:649px;top:1606px">Lorem ipsum dolor sit amet, consectetur adipisicing elit, sed do eiusmod tempor incididunt ut labore et dolore magna aliqua. Ut enim ad minim veniam, quis nostrud exercitation ullamco laboris nisi ut aliquip ex ea commodo consequat. Duis aute irure dolor in reprehenderit in voluptate velit esse cillum dolore eu fugiat nulla pariatur. Excepteur sint occaecat cupidatat non proident, sunt in culpa qui officia deserunt mollit anim id est laborum. Sed ut perspiciatis unde omnis iste natus error sit voluptatem accusantium doloremque laudantium, totam rem aperiam, eaque ipsa quae ab</p>
  <div class="abs btn" style="left:772px;top:1771px;width:214px;height:42px">LEARN MORE</div>

  <div class="abs hr" style="left:268px;top:1975px;width:688px;background:#666"></div>

  <section class="abs guide" style="left:77px;top:2021px">
    <h3>FINE JEWELLERY GUIDE</h3>
    <div class="photo" style="margin:26px auto 0;width:180px;height:174px;background:radial-gradient(circle,#d6d6d8,#f7f7f7 70%)" role="img" aria-label="Diamond hoop earrings, pendant necklace, studs and tennis bracelet"></div>
  </section>
  <p class="abs guide-text" style="left:99px;top:2264px">Lorem ipsum dolor sit amet, consectetur adipisicing elit, sed do eiusmod tempor incididunt ut labore et dolore magna aliqua. Ut enim ad minim veniam, quis nostrud exercitation ullamco laboris nisi ut aliquip ex ea commodo consequat. Duis aute irure dolor in reprehenderit in voluptate velit esse cillum dolore eu fugiat nulla pariatur. Excepteur sint occaecat cupidatat non proident, sunt in culpa qui officia deserunt mollit anim id est laborum. Sed ut perspiciatis unde omnis iste natus error sit voluptatem accusantium doloremque laudantium, totam rem aperiam, eaque ipsa quae ab</p>
  <div class="abs btn-small" style="left:170px;top:2362px">LEARN MORE</div>

  <section class="abs guide" style="left:474px;top:2018px">
    <h3>WEDDING RING GUIDE</h3>
    <div class="photo" style="margin:26px auto 0;width:160px;height:174px;background:radial-gradient(circle,#c9c9cc,#f7f7f7 70%)" role="img" aria-label="Solitaire engagement ring with matching floral wedding band"></div>
  </section>
  <p class="abs guide-text" style="left:497px;top:2260px">Lorem ipsum dolor sit amet, consectetur adipisicing elit, sed do eiusmod tempor incididunt ut labore et dolore magna aliqua. Ut enim ad minim veniam, quis nostrud exercitation ullamco laboris nisi ut aliquip ex ea commodo consequat. Duis aute irure dolor in reprehenderit in voluptate velit esse cillum dolore eu fugiat nulla pariatur. Excepteur sint occaecat cupidatat non proident, sunt in culpa qui officia deserunt mollit anim id est laborum. Sed ut perspiciatis unde omnis iste natus error sit voluptatem accusantium doloremque laudantium, totam rem aperiam, eaque ipsa quae ab</p>
  <div class="abs btn-small" style="left:568px;top:2359px">LEARN MORE</div>

  <section class="abs guide" style="left:842px;top:2018px">
    <h3>METAL EDUCATION</h3>
    <div class="photo" style="margin:26px auto 0;width:174px;height:174px;background:radial-gradient(circle,#cfc6bd,#f6f4f2 72%)" role="img" aria-label="Wedding bands in white, rose and yellow gold and grey metals"></div>
  </section>
  <p class="abs guide-text" style="left:857px;top:2260px">Lorem ipsum dolor sit amet, consectetur adipisicing elit, sed do eiusmod tempor incididunt ut labore et dolore magna aliqua. Ut enim ad minim veniam, quis nostrud exercitation ullamco laboris nisi ut aliquip ex ea commodo consequat. Duis aute irure dolor in reprehenderit in voluptate velit esse cillum dolore eu fugiat nulla pariatur. Excepteur sint occaecat cupidatat non proident, sunt in culpa qui officia deserunt mollit anim id est laborum. Sed ut perspiciatis unde omnis iste natus error sit voluptatem accusantium doloremque laudantium, totam rem aperiam, eaque ipsa quae ab</p>
  <div class="abs btn-small" style="left:928px;top:2359px">LEARN MORE</div>
</main>

<footer>
  <div class="abs newsletter">
    <div class="abs label" style="left:39px">STAY IN TOUCH</div>
    <div class="abs field">Please enter your email address</div>
    <div class="abs signup">SIGN UP</div>
    <div class="abs label" style="left:716px">OUR SOCIAL SIDE</div>
    <div class="abs social" style="left:961px"><span aria-label="Social page"></span><span aria-label="Photo page"></span><span aria-label="News feed"></span></div>
  </div>
  <div class="abs footer">
    <p class="abs about">Lorem ipsum dolor sit amet, consectetur adipisicing elit, sed do eiusmod tempor incididunt ut labore et dolore magna aliqua. Ut enim ad minim veniam, quis nostrud exercitation ullamco laboris nisi ut aliquip ex ea commodo consequat. Duis aute irure dolor in reprehenderit in voluptate velit esse cillum dolore eu fugiat nulla pariatur. Excepteur sint occaecat</p>
    <div class="abs help">Need Help?<br>
      <svg width="8" height="8" viewBox="0 0 8 8"><path d="M1 1l2 0 1 2-1 1c.5 1 1 1.5 2 2l1-1 2 1v2C4 8 0 4 1 1z" fill="#fff"/></svg>&nbsp; +61-000-555-010-020<br>
      <svg width="8" height="6" viewBox="0 0 8 6"><rect width="8" height="6" fill="#fff"/><path d="M0 0l4 3 4-3" stroke="#000" fill="none"/></svg>&nbsp; hello@quintora.example</div>
    <div class="abs col" style="left:571px"><h4>Account</h4>Sign up for an account<br>Terms and Conditions<br>Privacy Policy<br>Site Map</div>
    <div class="abs col" style="left:781px"><h4>About Us</h4>Our Story<br>Gift Wrap<br>Jewellery Care<br>Engraving</div>
    <div class="abs col" style="left:966px"><h4>Shopping Online</h4>Contact Us<br>Australia Delivery<br>International Delivery<br>Returns</div>
    <div class="abs copy">© 2018 Quintora Jewellers Australia</div>
  </div>
</footer>

</body>
</html>
```